BRM Going Cashless

Hello,
We are a medical office looking to get a flyer created to promote to our patients we will be going "Cashless." Our tagline will be "Cash-Less is Stress-Less"

"Starting in July, to offer you the fastest and most convenient service, we are transitioning to a cashless system. You can now enjoy faster checkout times and greater security with card and contactless payments. More info to come."

I've added two other flyers as sample designs we've used.

Please include logo, addresses, website, phone number

Files to include jpeg, png, pdf (under 5mb), Facebook and Instagram sizing.

Thank you,
Marlo

```html
<!DOCTYPE html>
<html lang="en">
<head>
<meta charset="utf-8">
<title>BRM – Cash-Less is Stress-Less</title>
<link rel="stylesheet" href="https://fonts.googleapis.com/css2?family=Montserrat:wght@800&family=Open+Sans:ital,wght@0,400;0,600;0,700;1,600&family=Sacramento&display=swap">
<style>
  :root {
    --page: #ffffff;
    --orange: #f07a45;
    --teal: #55c2a4;
    --teal-soft: #b9dcd8;
    --mist: #e9ecec;
    --ink: #2b2b2b;
    --body: #3a3a3a;
    --white: #ffffff;
  }
  * { box-sizing: border-box; margin: 0; padding: 0; }
  html, body { width: 1200px; height: 1200px; overflow: hidden; background: var(--page); }
  .flyer {
    position: absolute; left: 272px; top: 136px; width: 655px; height: 928px;
    overflow: hidden; background: var(--mist);
    font-family: "Open Sans", sans-serif;
  }
  .hero-photo {
    position: absolute; left: 0; top: 0; width: 655px; height: 440px;
    background: linear-gradient(160deg, #c9ccd0 0%, #8e939a 35%, #5a5f66 55%, #b7bbc0 80%, #d8dadd 100%);
  }
  .wave { position: absolute; left: 0; top: 370px; width: 655px; height: 320px; }
  .brand {
    position: absolute; left: 0; top: 70px; width: 655px;
    display: flex; align-items: center; justify-content: center; gap: 14px;
  }
  .brand-dot { width: 22px; height: 22px; border-radius: 50%; background: var(--teal); }
  .brand-name { font-family: "Open Sans", sans-serif; font-weight: 700; font-size: 56px; color: var(--orange); letter-spacing: 2px; }
  .tagline-script {
    position: absolute; left: 0; top: 290px; width: 655px; text-align: center;
    white-space: nowrap;
    font-family: "Sacramento", cursive; font-size: 160px; line-height: 1; color: var(--orange);
    letter-spacing: -3px;
    z-index: 2;
  }
  .tagline-main {
    position: absolute; left: 0; top: 452px; width: 655px; text-align: center;
    white-space: nowrap;
    font-family: "Montserrat", sans-serif; font-weight: 800; font-size: 74px; line-height: 1; color: var(--ink);
    letter-spacing: -1px;
    z-index: 1;
  }
  .start {
    position: absolute; left: 0; top: 538px; width: 655px; text-align: center;
    font-style: italic; font-weight: 600; font-size: 38px; line-height: 52px; color: var(--orange);
  }
  .message {
    position: absolute; left: 30px; top: 586px; width: 595px; text-align: center;
    font-size: 17.5px; line-height: 30px; color: var(--body);
  }
  .more { position: absolute; left: 0; top: 677px; width: 655px; text-align: center; font-style: italic; font-weight: 600; font-size: 18px; color: var(--orange); }
  .footer-band { position: absolute; left: 0; top: 725px; width: 655px; height: 203px; }
  .offices { position: absolute; left: 42px; top: 766px; width: 590px; display: flex; }
  .office { position: relative; padding-left: 16px; color: var(--white); font-size: 13.5px; line-height: 16.5px; }
  .office:nth-child(1) { width: 219px; }
  .office:nth-child(2) { width: 194px; }
  .office-name { color: var(--orange); font-weight: 700; font-size: 14.5px; line-height: 17px; }
  .pin { position: absolute; left: 0; top: 2px; width: 10px; height: 13px; }
  .divider { position: absolute; left: 47px; top: 842px; width: 570px; height: 1px; background: var(--orange); opacity: .7; }
  .contact { position: absolute; left: 87px; top: 861px; display: flex; align-items: flex-start; gap: 16px; }
  .contact-label { color: var(--white); font-weight: 700; font-size: 17.5px; margin-top: 12px; }
  .contact-phone { color: var(--orange); font-weight: 700; font-size: 34px; line-height: 36px; }
  .contact-web { color: var(--orange); font-size: 14px; letter-spacing: 3.6px; }
</style>
</head>
<body>
<main class="flyer">
  <div class="hero-photo" role="img" aria-label="Photo of a patient tapping a card on a payment terminal held at the front desk"></div>

  <svg class="wave" viewBox="0 0 655 320" preserveAspectRatio="none" aria-hidden="true">
    <defs>
      <linearGradient id="tealFade" x1="0" y1="0" x2="0" y2="1">
        <stop offset="0" stop-color="#a9d6d1"/>
        <stop offset="0.75" stop-color="#c6e0dd"/>
        <stop offset="1" stop-color="#e9ecec"/>
      </linearGradient>
    </defs>
    <path d="M0 32 C60 0 120 12 190 30 C260 48 290 22 340 20 C400 18 420 60 470 55 C540 48 600 50 655 38 L655 320 L0 320 Z" fill="url(#tealFade)"/>
    <path d="M60 10 C110 -4 150 8 200 26 C250 42 280 20 330 14 C380 10 400 48 440 52 C500 56 580 58 640 54 C590 68 500 70 450 66 C400 62 380 30 335 32 C285 36 260 60 200 46 C150 34 110 20 60 10 Z" fill="var(--teal)"/>
  </svg>

  <div class="brand">
    <span class="brand-dot"></span>
    <span class="brand-name">BRM</span>
  </div>

  <p class="tagline-script">Cash-Less</p>
  <h1 class="tagline-main">is Stress-Less</h1>

  <p class="start">Starting in July,</p>
  <p class="message">to offer you the fastest and most convenient service, we are transitioning to a cashless system. You can now enjoy faster checkout times and greater security with card and contactless payments.</p>
  <p class="more">More info to come.</p>

  <svg class="footer-band" viewBox="0 0 655 203" preserveAspectRatio="none" aria-hidden="true">
    <path d="M0 28 L18 22 L40 25 L62 18 L80 21 L96 12 L120 14 L138 8 L160 16 L182 10 L204 12 L222 4 L246 9 L262 3 L284 11 L300 6 L322 13 L340 7 L362 2 L380 10 L402 5 L424 12 L440 4 L462 9 L486 3 L506 11 L528 6 L548 13 L570 7 L592 12 L612 6 L634 10 L655 8 L655 203 L0 203 Z" fill="var(--ink)"/>
  </svg>

  <section class="offices">
    <div class="office">
      <svg class="pin" viewBox="0 0 10 13" aria-hidden="true"><path d="M5 0 C2.2 0 0 2.2 0 5 C0 8.5 5 13 5 13 C5 13 10 8.5 10 5 C10 2.2 7.8 0 5 0 Z M5 7 A2 2 0 1 1 5 3 A2 2 0 1 1 5 7 Z" fill="var(--orange)"/></svg>
      <p class="office-name">Northfield Office</p>
      <p>88 Harlow Park Dr.<br>Suite 120<br>Northfield, MD 20911</p>
    </div>
    <div class="office">
      <svg class="pin" viewBox="0 0 10 13" aria-hidden="true"><path d="M5 0 C2.2 0 0 2.2 0 5 C0 8.5 5 13 5 13 C5 13 10 8.5 10 5 C10 2.2 7.8 0 5 0 Z M5 7 A2 2 0 1 1 5 3 A2 2 0 1 1 5 7 Z" fill="var(--orange)"/></svg>
      <p class="office-name">Ashford Office</p>
      <p>450 Wellness Way<br>Ashford, WV 25990</p>
    </div>
    <div class="office">
      <svg class="pin" viewBox="0 0 10 13" aria-hidden="true"><path d="M5 0 C2.2 0 0 2.2 0 5 C0 8.5 5 13 5 13 C5 13 10 8.5 10 5 C10 2.2 7.8 0 5 0 Z M5 7 A2 2 0 1 1 5 3 A2 2 0 1 1 5 7 Z" fill="var(--orange)"/></svg>
      <p class="office-name">Lindale Office</p>
      <p>2175 Brookline Ave.<br>Ste. 305<br>Lindale, MD 20995</p>
    </div>
  </section>

  <div class="divider"></div>

  <div class="contact">
    <p class="contact-label">CONTRACT US TODAY</p>
    <div>
      <p class="contact-phone">(555) 014-2290</p>
      <p class="contact-web">www.brmcare.com</p>
    </div>
  </div>
</main>
</body>
</html>
```